依頼詳細
弊社の売りは
・様々な資格を所有したプロが必ず施工する事
・1980年創業 長年の技術と経験
・圧倒的な知識と技術力
・完全自社対応
・静岡県東部エリア限定の地域密着型
・迅速な対応

〇業務内容
害虫駆除サービス
・シロアリ
・スズメバチ
・ゴキブリ
・ノミ、ダニ
・その他

害獣駆除サービス
・ネズミ
・ハクビシン
・コウモリ
・鳥
・その他

ウィルス・除菌・消毒サービス
・除菌、抗菌(光触媒コーティング)
・殺菌、除菌(オゾン処理)
・消臭
・エアコンクリーニング
・その他

住宅環境改善サービス
・害虫.害獣侵入口閉鎖
・床下換気扇取付
・床下湿度改善
・換気口.基礎補修
・その他

記載項目
・はやせ消毒マーク
・会社名:株式会社はやせ消毒
・業務内容:依頼詳細を参考に省略して載せたいです
・役職:代表取締役
・名前(ローマ字):HAYASE KEIJI
・名前(漢字):早瀬 圭二
・本社:〒411-0957静岡県駿東郡長泉町上平原2231-15
・沼津営業所:〒410-0038静岡県沼津市北堀端2754-3
・E-mail:pct.hayase@kujonet-mail.jp
・フリーダイヤル:0120-387-519
・携帯:080-4938-2165

会社のサービス内容が解るイメージ、そして優しさと緊張感が融合してイメージ通りでした。

多くのご提案を頂きありがとうございました。
数少ない情報の中から一生懸命作っていただき感謝しております。
ありがとうございました。

```html
<!DOCTYPE html>
<html lang="ja">
<head>
<meta charset="utf-8">
<title>株式会社はやせ消毒 名刺</title>
<link rel="stylesheet" href="https://fonts.googleapis.com/css2?family=Noto+Sans+JP:wght@400;500;700&family=Roboto:wght@400;500&display=swap">
<style>
  :root{
    --page:#f1ece4;
    --card:#ffffff;
    --ink:#2a2a2a;
    --accent:#8a1a1a;
    --band:#6b1212;
    --panel:#e4e4e4;
    --icon:#3a3a3a;
    --rule:#555555;
  }
  *{margin:0;padding:0;box-sizing:border-box}
  html,body{width:752px;height:1200px;overflow:hidden;background:var(--page)}
  body{font-family:"Noto Sans JP",sans-serif;color:var(--ink)}
  .card{position:absolute;left:46px;top:18px;width:660px;height:1164px;background:var(--card);box-shadow:0 2px 10px rgba(0,0,0,.15)}
  .brand{position:absolute;right:26px;top:20px;display:flex;flex-direction:column;align-items:center;gap:8px}
  .brand-dot{width:96px;height:96px;border-radius:50%;background:var(--accent)}
  .brand-name{font-size:24px;font-weight:700;color:var(--accent)}
  .accent-bar{position:absolute;left:20px;top:216px;width:5px;height:100px;background:var(--accent)}
  .role{position:absolute;left:36px;top:222px;font-size:27px;font-weight:500}
  .name{position:absolute;left:36px;top:256px;display:flex;align-items:baseline;gap:22px}
  .name-kanji{font-size:52px;font-weight:500;letter-spacing:4px}
  .name-roman{font-family:"Roboto",sans-serif;font-size:24px;color:var(--accent);letter-spacing:1px}
  .contact{position:absolute;left:30px;top:340px;display:flex;gap:34px;font-family:"Roboto",sans-serif;font-size:23px}
  .contact span{display:flex;align-items:center;gap:8px}
  .office{position:absolute;left:30px;font-size:23px;line-height:35px}
  .office dt{color:var(--accent);font-weight:700}
  .office-head{top:400px}
  .office-branch{top:474px}
  .services{position:absolute;left:25px;top:572px;width:605px;height:392px;background:var(--panel);padding:18px 22px}
  .services-title{display:flex;align-items:center;gap:12px;font-size:25px;font-weight:500}
  .services-title::after{content:"";flex:1;height:2px;background:var(--rule)}
  .service{display:flex;align-items:flex-start;gap:16px;margin-top:18px}
  .service:first-of-type{margin-top:16px}
  .service-icon{width:48px;height:48px;background:var(--icon);flex-shrink:0;margin-top:6px}
  .service-name{font-size:28px;font-weight:500;color:var(--accent);line-height:34px}
  .service-note{font-size:19px;line-height:24px}
  .footer-band{position:absolute;left:0;bottom:0;width:660px;height:184px;background:var(--band);color:#fff;text-align:center;padding-top:26px}
  .company{font-size:32px;font-weight:700;letter-spacing:1px}
  .freedial{margin-top:16px;display:flex;justify-content:center;align-items:center;gap:12px;font-family:"Roboto",sans-serif;font-size:40px;font-weight:500}
</style>
</head>
<body>
<div class="card">
  <div class="brand">
    <div class="brand-dot"></div>
    <div class="brand-name">はやせ消毒</div>
  </div>

  <div class="accent-bar"></div>
  <p class="role">代表取締役</p>
  <p class="name"><span class="name-kanji">早瀬 圭二</span><span class="name-roman">HAYASE KEIJI</span></p>

  <div class="contact">
    <span><svg width="18" height="24" viewBox="0 0 18 24"><rect x="1" y="1" width="16" height="22" rx="3" fill="none" stroke="#2a2a2a" stroke-width="2"/><circle cx="9" cy="19" r="1.5" fill="#2a2a2a"/></svg>080-4938-2165</span>
    <span><svg width="26" height="18" viewBox="0 0 26 18"><rect width="26" height="18" fill="#2a2a2a"/><path d="M1 1 L13 10 L25 1" fill="none" stroke="#fff" stroke-width="2"/></svg>pct.hayase@kujonet-mail.jp</span>
  </div>

  <dl class="office office-head">
    <dt>本社：</dt>
    <dd>〒411-0957 静岡県駿東郡長泉町上平原2231-15</dd>
  </dl>
  <dl class="office office-branch">
    <dt>沼津営業所：</dt>
    <dd>〒410-0038 静岡県沼津市北堀端2754-3</dd>
  </dl>

  <section class="services">
    <h2 class="services-title">業務内容</h2>
    <div class="service">
      <div class="service-icon" role="img" aria-label="害虫駆除のアイコン"></div>
      <div><p class="service-name">害虫駆除サービス</p><p class="service-note">シロアリ、スズメバチ、ゴキブリなど</p></div>
    </div>
    <div class="service">
      <div class="service-icon" role="img" aria-label="害獣駆除のアイコン"></div>
      <div><p class="service-name">害獣駆除サービス</p><p class="service-note">ネズミ、ハクビシン、コウモリなど</p></div>
    </div>
    <div class="service">
      <div class="service-icon" role="img" aria-label="除菌・消毒のアイコン"></div>
      <div><p class="service-name">ウィルス・除菌・消毒サービス</p><p class="service-note">光触媒コーティング、オゾン処理、エアコンクリーニング</p></div>
    </div>
    <div class="service">
      <div class="service-icon" role="img" aria-label="住宅環境改善のアイコン"></div>
      <div><p class="service-name">住宅環境改善サービス</p><p class="service-note">害虫.害獣侵入口閉鎖・換気口.基礎補修</p></div>
    </div>
  </section>

  <footer class="footer-band">
    <p class="company">株式会社はやせ消毒</p>
    <p class="freedial">
      <svg width="48" height="28" viewBox="0 0 48 28"><rect x="1" y="1" width="46" height="26" rx="4" fill="none" stroke="#fff" stroke-width="2"/><circle cx="15" cy="14" r="7" fill="none" stroke="#fff" stroke-width="3"/><circle cx="33" cy="14" r="7" fill="none" stroke="#fff" stroke-width="3"/></svg>
      0120-387-519
    </p>
  </footer>
</div>
</body>
</html>
```